Tall Harbor Business Card

We are a Video Production and Video Equipment Rental company specialising in the supply of state of the art Video Technology and Services for the Live Entertainment, Television and Corporate Business Theatre markets. (in Sydney, Australia) www.tallharbor.example

Industry/Entity Type

Business

Contact Information for Business Card

name, position, email, website, address, logo
Example attached of the information we need - doesn't necessarily have to look the same

Font styles to use
Other font styles liked:
• Tall Harbor logo font is GOTHAM

Colors
ea1f27

Requirements
Nice to have
• either matt black or shiny black cards -
raised logo

```html
<!DOCTYPE html>
<html lang="en">
<head>
<meta charset="utf-8">
<title>Tall Harbor Business Card</title>
<link rel="stylesheet" href="https://fonts.googleapis.com/css2?family=Montserrat:wght@400;500;600;700&display=swap">
<style>
  :root {
    --stage: #1b1a19;
    --card: #161616;
    --card-light: #222222;
    --red: #ea1f27;
    --white: #f2f2f2;
    --silver: #c9c9c9;
    --grey: #9a9a9a;
  }
  * { box-sizing: border-box; margin: 0; padding: 0; }
  html, body { width: 1200px; height: 716px; overflow: hidden; }
  body {
    background: var(--stage);
    font-family: "Montserrat", Arial, sans-serif;
    position: relative;
  }
  .card {
    position: absolute;
    top: 208px;
    width: 520px;
    height: 300px;
    border-radius: 3px;
    overflow: hidden;
    box-shadow: 0 10px 30px rgba(0,0,0,.55);
  }
  .card-front { left: 50px; }
  .card-back { left: 630px; }
  .card-texture {
    position: absolute; inset: 0;
    background: linear-gradient(135deg, var(--card-light) 0%, var(--card) 60%, #101010 100%);
  }
  .front-logo {
    position: absolute; left: 34px; top: 48px;
    display: flex; align-items: center; gap: 10px;
  }
  .logo-square { width: 10px; height: 10px; background: var(--red); }
  .logo-name {
    color: var(--white); font-weight: 600; font-size: 26px; letter-spacing: .5px;
    text-transform: uppercase;
  }
  .divider {
    position: absolute; left: 262px; top: 40px; width: 1px; height: 172px;
    background: var(--grey);
  }
  .contact { position: absolute; left: 282px; top: 48px; }
  .contact-name {
    color: var(--red); font-weight: 600; font-size: 21px; text-transform: uppercase; letter-spacing: .5px;
  }
  .contact-role {
    color: var(--white); font-size: 11px; font-weight: 500; text-transform: uppercase;
    letter-spacing: .5px; margin-bottom: 14px;
  }
  .contact-list { list-style: none; }
  .contact-list li {
    color: var(--white); font-size: 12px; line-height: 18px;
    display: flex; align-items: flex-start; gap: 7px;
  }
  .contact-list svg { flex: none; margin-top: 4px; }
  .contact-list .indent { padding-left: 17px; }
  .service-band {
    position: absolute; left: 0; right: 0; bottom: 48px; height: 32px;
    background: var(--red);
    color: var(--white); font-size: 11.5px; font-weight: 500; text-transform: uppercase;
    letter-spacing: .3px; display: flex; align-items: center; padding-left: 26px;
  }
  .back-logo {
    position: absolute; inset: 0;
    display: flex; align-items: center; justify-content: center; gap: 16px;
  }
  .back-logo .logo-square { width: 16px; height: 16px; }
  .back-logo .logo-name { font-size: 52px; color: var(--silver); letter-spacing: 1px; }
</style>
</head>
<body>
  <section class="card card-front" aria-label="Business card front">
    <div class="card-texture" role="img" aria-label="Black card surface with faint triangular texture"></div>
    <div class="front-logo">
      <span class="logo-square"></span>
      <span class="logo-name">Tall Harbor</span>
    </div>
    <div class="divider"></div>
    <div class="contact">
      <p class="contact-name">Sam Delaney</p>
      <p class="contact-role">Managing Director</p>
      <ul class="contact-list">
        <li><svg width="10" height="10" viewBox="0 0 10 10"><rect width="10" height="10" rx="1.5" fill="#ea1f27"/><path d="M3 2.2l1 1.8-.7.7a4 4 0 0 0 2 2l.7-.7 1.8 1-.5 1A5 5 0 0 1 2 3z" fill="#fff"/></svg>0400 118 226</li>
        <li><svg width="10" height="10" viewBox="0 0 10 10"><rect width="10" height="10" rx="1.5" fill="#ea1f27"/><path d="M2 3h6v4H2zM2 3l3 2.3L8 3" fill="none" stroke="#fff" stroke-width=".9"/></svg>mail@tallharbor.example</li>
        <li><svg width="10" height="10" viewBox="0 0 10 10"><rect width="10" height="10" rx="1.5" fill="#ea1f27"/><circle cx="5" cy="5" r="2.8" fill="none" stroke="#fff" stroke-width=".9"/><path d="M2.2 5h5.6M5 2.2v5.6" stroke="#fff" stroke-width=".7"/></svg>www.tallharbor.example</li>
        <li><svg width="10" height="10" viewBox="0 0 10 10"><rect width="10" height="10" rx="1.5" fill="#ea1f27"/><path d="M5 8.3S2.6 5.6 2.6 4.1a2.4 2.4 0 0 1 4.8 0C7.4 5.6 5 8.3 5 8.3z" fill="#fff"/></svg>12 Quay Lane,</li>
        <li class="indent">Harbourside, Sydney</li>
      </ul>
    </div>
    <div class="service-band">Video Solutions-LED Screens-Camera Systems-Projection</div>
  </section>

  <section class="card card-back" aria-label="Business card back">
    <div class="card-texture" role="img" aria-label="Black card surface with faint triangular texture"></div>
    <div class="back-logo">
      <span class="logo-square"></span>
      <span class="logo-name">Tall Harbor</span>
    </div>
  </section>
</body>
</html>
```